Wine Label for new family wine label

we need a new wine label and name for our new group winemaking project. There are 10 of us in the group, plus two wine growers and two winemakers. We will be making wines on an ongoing basis but relatively small scale. The wines will be coming from the barossa valley and coonawarra. They will be high end wines - built on great dirt, some great history with the growers, and ultimately great grapes. We will be initially producing 4 wines, a shiraz, a cab, and a blend plus one high end single block shiraz based wine.

We are looking for the wine label to reflect quality, family and friendship.

```html
<!DOCTYPE html>
<html lang="en">
<head>
<meta charset="utf-8">
<title>Cedar Row Shiraz Cabernet Label</title>
<link rel="stylesheet" href="https://fonts.googleapis.com/css2?family=Cormorant+Garamond:wght@500&family=Cormorant+SC:wght@500&display=swap">
<style>
  :root {
    --backdrop: #dcdde0;
    --label-black: #000000;
    --rule-white: #ffffff;
    --text-white: #ffffff;
    --gold: #e2a726;
  }
  html, body {
    margin: 0;
    padding: 0;
    width: 1200px;
    height: 1000px;
    overflow: hidden;
    background: var(--backdrop);
  }
  .wine-label {
    position: absolute;
    left: 260px;
    top: 205px;
    width: 680px;
    height: 590px;
    background: var(--label-black);
    text-align: center;
  }
  .rule {
    position: absolute;
    left: 0;
    width: 100%;
    height: 3px;
    background: var(--rule-white);
  }
  .rule--top { top: 40px; }
  .rule--bottom { top: 551px; }
  .wine-name {
    position: absolute;
    left: 0;
    width: 100%;
    top: 180px;
    margin: 0;
    font-family: "Cormorant Garamond", serif;
    font-weight: 500;
    font-size: 104px;
    line-height: 1;
    color: var(--text-white);
  }
  .varietal {
    position: absolute;
    left: 0;
    width: 100%;
    top: 374px;
    margin: 0;
    font-family: "Cormorant SC", serif;
    font-weight: 500;
    font-size: 42px;
    letter-spacing: 1.5px;
    line-height: 1;
    color: var(--gold);
  }
  .region {
    position: absolute;
    left: 0;
    width: 100%;
    top: 432px;
    margin: 0;
    font-family: "Cormorant Garamond", serif;
    font-weight: 500;
    font-size: 19px;
    letter-spacing: 3.2px;
    line-height: 1;
    color: var(--gold);
  }
  .vintage {
    position: absolute;
    left: 0;
    width: 100%;
    top: 486px;
    margin: 0;
    font-family: "Cormorant Garamond", serif;
    font-weight: 500;
    font-size: 30px;
    letter-spacing: 6px;
    line-height: 1;
    color: var(--text-white);
  }
</style>
</head>
<body>
  <main class="wine-label">
    <div class="rule rule--top"></div>
    <h1 class="wine-name">Cedar Row</h1>
    <p class="varietal">Shiraz Cabernet</p>
    <p class="region">BAROSSA VALLEY AND COONAWARRA</p>
    <p class="vintage">2014</p>
    <div class="rule rule--bottom"></div>
  </main>
</body>
</html>
```